I need the Scorecard I've developed for my staff to be produced into a visually engaging piece that will encourage the staff to utilize it on a daily basis. I'm thinking it could be 5x7 in size so that it isn't too cumbersome, but I'm open to different layouts.
I have multiple other departments that will need Scorecards created for them as well, but each one will contain task specific questions for each department.

```html
<!DOCTYPE html>
<html lang="en">
<head>
<meta charset="UTF-8">
<title>Receptionist Daily Excellence Scorecard</title>
<link href="https://fonts.googleapis.com/css2?family=Montserrat:wght@600;700&family=Figtree:wght@400;500;700&display=swap" rel="stylesheet">
<style>
  :root {
    --backdrop: #e6e7ea;
    --page-blue: #2079f6;
    --deep-blue: #0661f2;
    --band-blue: #0762f1;
    --card: #ffffff;
    --row-tint: #dde9fd;
    --ink: #2a2f3a;
    --label-blue: #0b63f0;
    --box-line: #9aa0aa;
    --white: #ffffff;
  }
  * { box-sizing: border-box; margin: 0; padding: 0; }
  html, body { width: 1200px; height: 756px; overflow: hidden; }
  body {
    background: var(--backdrop);
    position: relative;
    font-family: "Figtree", sans-serif;
    color: var(--ink);
  }
  .page {
    position: absolute;
    top: 87px;
    width: 399px;
    height: 563px;
    background: var(--page-blue);
    overflow: hidden;
  }
  .page--front { left: 167px; }
  .page--back { left: 637px; }
  .page-glow {
    position: absolute;
    inset: 0;
    background: radial-gradient(circle at 50% 95%, rgba(12, 95, 235, 0.55) 0%, rgba(32, 121, 246, 0) 65%);
  }
  .page--back .page-glow {
    background: radial-gradient(circle at 50% 50%, rgba(12, 95, 235, 0.45) 0%, rgba(32, 121, 246, 0) 70%);
  }
  .corner-disc { position: absolute; left: 0; top: 0; }
  .title {
    position: absolute;
    left: 50px;
    top: 52px;
    font-family: "Montserrat", sans-serif;
    font-weight: 700;
    font-size: 19.5px;
    line-height: 23px;
    color: var(--white);
  }
  .identity {
    position: absolute;
    left: 50px;
    top: 113px;
    color: var(--white);
    font-size: 10.5px;
    line-height: 14px;
  }
  .identity span { display: inline-block; width: 42px; }
  .rating-guide {
    position: absolute;
    left: 50px;
    top: 192px;
    color: var(--white);
    font-size: 8.6px;
    line-height: 12.1px;
  }
  .section { position: absolute; left: 23px; width: 353px; }
  .section-band {
    position: absolute;
    left: 9px;
    top: 0;
    width: 327px;
    height: 26px;
    background: var(--band-blue);
    border-radius: 4px;
    color: var(--white);
    font-family: "Montserrat", sans-serif;
    font-weight: 700;
    font-size: 9px;
    line-height: 26px;
    padding-left: 13px;
    z-index: 2;
  }
  .section-card {
    margin-top: 15px;
    background: var(--card);
    border-radius: 8px;
    padding: 19px 0 12px;
  }
  .task-head {
    position: relative;
    height: 12px;
    font-size: 6.4px;
    font-weight: 700;
    line-height: 12px;
    margin-bottom: 3.25px;
  }
  .task-head .col-task { position: absolute; left: 24px; color: var(--label-blue); }
  .task-head .col-rating { position: absolute; left: 197px; }
  .task-head .col-notes { position: absolute; left: 269px; }
  .task-row { position: relative; height: 15.5px; font-size: 7.6px; line-height: 15.5px; }
  .task-row--tint::before {
    content: "";
    position: absolute;
    left: 9px;
    top: 0.75px;
    width: 184px;
    height: 14px;
    border-radius: 7px;
    background: var(--row-tint);
  }
  .task-name { position: absolute; left: 24px; }
  .rating-box, .notes-box {
    position: absolute;
    top: 2.75px;
    height: 10px;
    border: 0.8px solid var(--box-line);
    border-radius: 2px;
    background: var(--white);
  }
  .rating-box { left: 210px; width: 30px; }
  .notes-box { left: 258px; width: 68px; }
</style>
</head>
<body>

<section class="page page--front">
  <div class="page-glow" role="img" aria-label="Soft radiating light burst behind the scorecard sections"></div>
  <svg class="corner-disc" width="399" height="563" viewBox="0 0 399 563" aria-hidden="true">
    <circle cx="366.5" cy="43.5" r="118" fill="none" stroke="#0a5ee6" stroke-width="0.8"/>
    <circle cx="366.5" cy="43.5" r="103" fill="var(--deep-blue)"/>
  </svg>

  <h1 class="title">Receptionist Daily<br>Excellence Scorecard</h1>

  <div class="identity">
    <p><span>Name</span>:</p>
    <p><span>Date</span>:</p>
    <p><span>location</span>:</p>
  </div>

  <div class="rating-guide">
    <p>Please rate yourself for each task:</p>
    <p>1 = Needs Improvement,</p>
    <p>3 = Meets Expectations,</p>
    <p>5 = Excellent</p>
  </div>

  <div class="section" style="top:261px;">
    <div class="section-band">1. Call Handling &amp; First Call Intake</div>
    <div class="section-card">
      <div class="task-head"><span class="col-task">Task :</span><span class="col-rating">Self-Rating (1-5)</span><span class="col-notes">Notes / Issues</span></div>
      <div class="task-row"><span class="task-name">Answered 90%+ calls within 3 rings</span><span class="rating-box"></span><span class="notes-box"></span></div>
      <div class="task-row task-row--tint"><span class="task-name">Maintained empathy and professionalism</span><span class="rating-box"></span><span class="notes-box"></span></div>
      <div class="task-row"><span class="task-name">Accurately completed all First Call fields</span><span class="rating-box"></span><span class="notes-box"></span></div>
      <div class="task-row task-row--tint"><span class="task-name">Worked within Receptionist role</span><span class="rating-box"></span><span class="notes-box"></span></div>
    </div>
  </div>

  <div class="section" style="top:402px;">
    <div class="section-band">2. Call Management During Busy Times</div>
    <div class="section-card">
      <div class="task-head"><span class="col-task">Task :</span><span class="col-rating">Self-Rating (1-5)</span><span class="col-notes">Notes / Issues</span></div>
      <div class="task-row"><span class="task-name">Prioritized urgent vs. non-urgent calls</span><span class="rating-box"></span><span class="notes-box"></span></div>
      <div class="task-row task-row--tint"><span class="task-name">Hold times under 1 minute</span><span class="rating-box"></span><span class="notes-box"></span></div>
      <div class="task-row"><span class="task-name">Logged all calls</span><span class="rating-box"></span><span class="notes-box"></span></div>
      <div class="task-row task-row--tint"><span class="task-name">Requested help if overwhelmed</span><span class="rating-box"></span><span class="notes-box"></span></div>
    </div>
  </div>
</section>

<section class="page page--back">
  <div class="page-glow" role="img" aria-label="Soft radiating light burst behind the scorecard sections"></div>

  <div class="section" style="top:27.5px;">
    <div class="section-band">3. cheduling Accuracy</div>
    <div class="section-card">
      <div class="task-head"><span class="col-task">Task :</span><span class="col-rating">Self-Rating (1-5)</span><span class="col-notes">Notes / Issues</span></div>
      <div class="task-row"><span class="task-name">Updated scheduling board</span><span class="rating-box"></span><span class="notes-box"></span></div>
      <div class="task-row task-row--tint"><span class="task-name">Cross-checked with Red Book</span><span class="rating-box"></span><span class="notes-box"></span></div>
      <div class="task-row"><span class="task-name">Entered manifold info promptly</span><span class="rating-box"></span><span class="notes-box"></span></div>
    </div>
  </div>

  <div class="section" style="top:146.5px;">
    <div class="section-band">4. Clothing &amp; Flowers</div>
    <div class="section-card">
      <div class="task-head"><span class="col-task">Task :</span><span class="col-rating">Self-Rating (1-5)</span><span class="col-notes">Notes / Issues</span></div>
      <div class="task-row"><span class="task-name">Clothing sheet completed</span><span class="rating-box"></span><span class="notes-box"></span></div>
      <div class="task-row task-row--tint"><span class="task-name">Family contact noted on sheet</span><span class="rating-box"></span><span class="notes-box"></span></div>
      <div class="task-row"><span class="task-name">Floral deliveries logged</span><span class="rating-box"></span><span class="notes-box"></span></div>
      <div class="task-row task-row--tint"><span class="task-name">Concerns communicated to Care Center</span><span class="rating-box"></span><span class="notes-box"></span></div>
      <div class="task-row"><span class="task-name">Flower placement verified</span><span class="rating-box"></span><span class="notes-box"></span></div>
    </div>
  </div>

  <div class="section" style="top:292.5px;">
    <div class="section-band">5. Death Certificates</div>
    <div class="section-card">
      <div class="task-head"><span class="col-task">Task :</span><span class="col-rating">Self-Rating (1-5)</span><span class="col-notes">Notes / Issues</span></div>
      <div class="task-row"><span class="task-name">Verified recipient ID &amp; relationship</span><span class="rating-box"></span><span class="notes-box"></span></div>
      <div class="task-row task-row--tint"><span class="task-name">Confirmed correct documents enclosed</span><span class="rating-box"></span><span class="notes-box"></span></div>
      <div class="task-row"><span class="task-name">Recipient signed the DC logbook</span><span class="rating-box"></span><span class="notes-box"></span></div>
      <div class="task-row task-row--tint"><span class="task-name">Suggested proofreading before leaving</span><span class="rating-box"></span><span class="notes-box"></span></div>
    </div>
  </div>

  <div class="section" style="top:428.5px;">
    <div class="section-band">3. Scheduling Accuracy</div>
    <div class="section-card">
      <div class="task-head"><span class="col-task">Task :</span><span class="col-rating">Self-Rating (1-5)</span><span class="col-notes">Notes / Issues</span></div>
      <div class="task-row"><span class="task-name">Updated scheduling board</span><span class="rating-box"></span><span class="notes-box"></span></div>
      <div class="task-row task-row--tint"><span class="task-name">Cross-checked with Red Book</span><span class="rating-box"></span><span class="notes-box"></span></div>
      <div class="task-row"><span class="task-name">Entered manifold info promptly</span><span class="rating-box"></span><span class="notes-box"></span></div>
    </div>
  </div>
</section>

</body>
</html>
```